Silver Fern Apothecary needs a label design or modification for new Kratom Co., need simple, eye catch

New company in Northern California that is going wholesale and retail for Kratom, a natural alternative from todays pharmaceutical drugs, we want to provide a better quality product than what the public in our area is generally exposed to, and eventually wider than Northern California

We need a better, eye catching, simple label design for our new Kratom line at Silver Fern Apothecary
This line will be Kratom that is harvested from the "Wild"....or "Forest Grown"
attached are files for capsule bottles, would like to be similar, but i don't feel the label "pops" or will grab enough attention.
It will be for Kratom ultra fine powder of premium grade, no stems and veins or any other additives or fillers

The existing Logo was created by pixel forge and would like it to be used
maybe with a graphic drawing of a Kratom leaf in the background ? not sure.
We are open to new ideas.

Maybe the label needs to be totally different, not sure.
Saw a friends project from pixel forge for Kratom, it was simple and i loved it, maybe even reduce the number of colors, maybe not
need the files in "AI" and would be nice if layered
there will be two different sizes
100g (3.527 oz) needs to be in the lower third of the bottom, in an area of
4 1/2" x 6"
50g (1.764 oz) in an area of 3 3/8" x 4"
The number declarations need to be at least 3/16" tall
as you will see from the attached files, some have green, red or white colors on the top and bottom of the label, this is to help the eye better catch the general type of strain for the customer and for the people selling the product
all other needed info will be in the attached files

The attached files are for Tortoise Kratom Tablets, the newer product is for Summit Kratom Blend (or maybe Select Kratom Blend), of various types.
Our product is better than most others and usually much stronger.
We provide consistency of product quality, which is hard to find with this item.

When printed "Silver Fern" doesnt stand out, especially with a black background, the black may make the printing of the gold darker than what it should be. Not sure if "Silver Fern" would be appropriate in white, or if i need a new design.

The Type of each kind may be added later simply because we carry so many different kinds, and as is said, we are open to new ideas.
Thank You

Target Market(s)

General public through wholesale to retailers, Kratom community

Industry/Entity Type

It Company

Font styles to use
Sans Serif
Other font styles liked:
• segoe print

Colors
fece3e
abd036
ec1f27
ffffff

Requirements
Must have
• size declarations of at least 3/16"
• and be taller than wide
Nice to have
• graphic picture of a Kratom leaf
Should not have
• for human consumption

```html
<!DOCTYPE html>
<html lang="en">
<head>
<meta charset="utf-8">
<title>Silver Fern Apothecary – Select Kratom Blend Label</title>
<link rel="stylesheet" href="https://fonts.googleapis.com/css2?family=Josefin+Sans:wght@500&family=Teko:wght@500;600&family=Oswald:wght@400&display=swap">
<style>
  :root {
    --stage: #f1f1f1;
    --label-black: #050505;
    --label-green-glow: #0d3a1e;
    --brand-gold: #fece3e;
    --leaf-green: #abd036;
    --kratom-green: #3fbf3a;
    --ring-green: #22a83a;
    --strain-red: #ec1f27;
    --white: #ffffff;
    --photo-brown: #7a4a2a;
    --photo-green: #6aa83a;
  }
  * { margin: 0; padding: 0; box-sizing: border-box; }
  html, body { width: 1200px; height: 662px; overflow: hidden; background: var(--stage); }
  .canvas { position: relative; width: 1200px; height: 662px; }

  .label {
    position: absolute; left: 395px; top: 58px;
    width: 410px; height: 546px; overflow: hidden;
    background:
      radial-gradient(ellipse 70% 45% at 50% 40%, var(--label-green-glow) 0%, transparent 70%),
      linear-gradient(160deg, transparent 30%, rgba(40,140,70,0.18) 45%, transparent 55%),
      var(--label-black);
  }
  .strain-band { position: absolute; left: 0; width: 100%; }
  .strain-band.top {
    top: 0; height: 40px;
    background: linear-gradient(to bottom, var(--strain-red) 0 6px, rgba(236,31,39,0.55) 6px, transparent 100%);
  }
  .strain-band.bottom {
    bottom: 0; height: 60px;
    background: linear-gradient(to top, rgba(236,31,39,0.75) 0%, rgba(236,31,39,0.25) 55%, transparent 100%);
  }

  .logo-ring { position: absolute; left: 0; top: 0; }

  .brand-mark {
    position: absolute; left: 160px; top: 72px;
    width: 90px; height: 90px; border-radius: 50%;
    background: var(--brand-gold);
  }

  .brand-name {
    position: absolute; left: 0; width: 100%; text-align: center;
    font-family: "Josefin Sans", sans-serif; font-weight: 500;
    color: var(--brand-gold); line-height: 1; text-transform: uppercase;
  }
  .brand-name.primary { top: 190px; font-size: 38px; }
  .brand-name.secondary { top: 236px; font-size: 23px; letter-spacing: 1px; }

  .natural-seal { position: absolute; left: 307px; top: 279px; }

  .product-line {
    position: absolute; left: 0; width: 100%; text-align: center;
    font-family: "Teko", sans-serif; font-weight: 600; line-height: 1; text-transform: uppercase;
  }
  .product-line.grade { top: 322px; font-size: 36px; color: var(--white); }
  .product-line.name { top: 352px; font-size: 48px; color: var(--kratom-green); letter-spacing: 1px; }

  .claims {
    position: absolute; left: 0; top: 403px; width: 100%;
    display: flex; justify-content: center; gap: 14px;
    font-family: "Oswald", sans-serif; font-size: 12px; color: var(--strain-red);
    text-transform: uppercase;
  }
  .claim { display: flex; align-items: center; gap: 5px; }

  .product-photo {
    position: absolute; left: 116px; top: 430px; width: 190px; height: 96px;
    border-radius: 8px;
    background: linear-gradient(to bottom, var(--photo-green), var(--photo-brown));
  }

  .net-weight {
    position: absolute; left: 150px; top: 525px; width: 110px; height: 21px;
    background: var(--strain-red); border-radius: 6px 6px 0 0;
    font-family: "Oswald", sans-serif; font-size: 12px; font-weight: 400;
    color: var(--white); text-align: center; line-height: 21px;
  }
</style>
</head>
<body>
<div class="canvas">
  <section class="label">
    <div class="strain-band top"></div>
    <div class="strain-band bottom"></div>

    <svg class="logo-ring" width="410" height="546" viewBox="0 0 410 546" aria-hidden="true">
      <path d="M 120 130 A 104 104 0 1 0 290 130" fill="none" stroke="var(--ring-green)" stroke-width="2.5"/>
    </svg>

    <div class="brand-mark" aria-hidden="true"></div>
    <div class="brand-name primary">Silver Fern</div>
    <div class="brand-name secondary">Apothecary</div>

    <svg class="natural-seal" width="54" height="54" viewBox="0 0 54 54" aria-hidden="true">
      <circle cx="27" cy="27" r="25" fill="none" stroke="var(--ring-green)" stroke-width="2"/>
    </svg>

    <div class="product-line grade">Select</div>
    <div class="product-line name">Kratom Blend</div>

    <div class="claims">
      <span class="claim">
        <svg width="16" height="16" viewBox="0 0 16 16" aria-hidden="true"><circle cx="8" cy="8" r="8" fill="var(--white)"/><path d="M4.5 8.2 7 10.5 11.5 5.5" fill="none" stroke="#222" stroke-width="1.6"/></svg>
        No additives
      </span>
      <span class="claim">
        <svg width="16" height="16" viewBox="0 0 16 16" aria-hidden="true"><circle cx="8" cy="8" r="8" fill="var(--white)"/><path d="M4.5 8.2 7 10.5 11.5 5.5" fill="none" stroke="#222" stroke-width="1.6"/></svg>
        No fillers
      </span>
    </div>

    <div class="product-photo" role="img" aria-label="Photo of a wooden bowl of green kratom powder with a spoon and fresh leaves"></div>

    <div class="net-weight">100G (3.527 OZ)</div>
  </section>
</div>
</body>
</html>
```